Business Card design for construction company

I would like a business card design for a construction company - Harlow Constructions. I have attached the ai logo file for use. I would like the card to be very smart and clean and incorporate only white and the two colours in the logo. I would like the card to have two sides. One side can just have the logo, the other with the relevant information.

Target Market(s)

Building and Construction Clients

Industry/Entity Type

Business

Contact Information for Business Card

Name: Tom Pardoe
Company: Harlow Constructions Pty Limited
Address: 14 Mallee Crescent Carrow Vale 2093
Phone: 0427 531 068
Email: tomp@harlowbuild-example.com.au

Font styles to use
Serif
Sans Serif

Requirements
Must have
• Details noted above
• Logo as provided
• Colours as in logo
• Square edges
• A font that compliments the logo
Should not have
• Any colour other than white and those in logo
• Rounded edges

```html
<!DOCTYPE html>
<html lang="en">
<head>
<meta charset="utf-8">
<title>Harlow Constructions – Business Card</title>
<link rel="stylesheet" href="https://fonts.googleapis.com/css2?family=Michroma&family=Open+Sans:wght@400;700&display=swap">
<style>
  :root {
    --backdrop: #2a2a2b;
    --card-dark: #4b4b4d;
    --card-light: #ffffff;
    --brand-blue: #1b8fd0;
    --ink-grey: #4b4b4d;
    --shadow: rgba(0, 0, 0, 0.45);
  }
  * { box-sizing: border-box; margin: 0; padding: 0; }
  html, body {
    width: 1200px;
    height: 900px;
    overflow: hidden;
    background: var(--backdrop);
  }
  .stage {
    position: relative;
    width: 1200px;
    height: 900px;
  }
  .card {
    position: absolute;
    width: 640px;
    height: 366px;
    box-shadow: 0 14px 30px var(--shadow);
    overflow: hidden;
  }
  .card--front { left: 220px; top: 70px; background: var(--card-dark); }
  .card--back  { left: 340px; top: 464px; background: var(--card-light); }

  .wordmark {
    position: absolute;
    display: flex;
    align-items: center;
    gap: 18px;
  }
  .wordmark__square {
    width: 22px;
    height: 22px;
    background: var(--brand-blue);
    flex: none;
  }
  .wordmark__name {
    font-family: "Michroma", sans-serif;
    font-size: 25px;
    letter-spacing: 2px;
    white-space: nowrap;
  }
  .card--front .wordmark { left: 54px; top: 168px; }
  .card--front .wordmark__name { color: var(--card-light); }
  .card--back .wordmark { left: 54px; top: 176px; }
  .card--back .wordmark__name { color: var(--ink-grey); }

  .holder {
    position: absolute;
    left: 96px;
    top: 74px;
    font-family: "Michroma", sans-serif;
  }
  .holder__name {
    color: var(--ink-grey);
    font-size: 17px;
    letter-spacing: 1px;
  }
  .holder__role {
    color: var(--brand-blue);
    font-size: 12px;
    letter-spacing: 1.5px;
    margin-top: 2px;
  }

  .contact {
    position: absolute;
    right: 40px;
    bottom: 58px;
    text-align: right;
    font-family: "Open Sans", sans-serif;
    color: var(--ink-grey);
    font-size: 15px;
    line-height: 1.35;
  }
  .contact__company {
    color: var(--brand-blue);
    font-weight: 700;
  }
  .contact__line--phone { font-size: 17px; margin-top: 2px; }
</style>
</head>
<body>
  <main class="stage">
    <section class="card card--front" aria-label="Business card front">
      <div class="wordmark">
        <span class="wordmark__square"></span>
        <span class="wordmark__name">HARLOW CONSTRUCTIONS</span>
      </div>
    </section>

    <section class="card card--back" aria-label="Business card back">
      <div class="holder">
        <p class="holder__name">TOM PARDOE</p>
        <p class="holder__role">MANAGING DIRECTOR</p>
      </div>
      <div class="wordmark">
        <span class="wordmark__square"></span>
        <span class="wordmark__name">HARLOW CONSTRUCTIONS</span>
      </div>
      <address class="contact">
        <p class="contact__company">Harlow Constructions Pty Limited</p>
        <p class="contact__line">14 Mallee Crescent Carrow Vale 2093</p>
        <p class="contact__line contact__line--phone">0427 531 068 | tomp@harlowbuild-example.com.au</p>
      </address>
    </section>
  </main>
</body>
</html>
```